Design for Torvel Ginger Chewy Candy!

Hello! We are Torvel Enterprises Corp, a food manufacturer and distributor based in Los Angeles, CA. We manufacture Chips, Cookies, Juices, Dairy, and last but not least, Candies! We are launching our Ginger Chewy Candy soon and we need a great design for it!

Our Ginger Chewy Candy is a perfect mixture between sweet and spicy from the ginger itself. Torvel Ginger Chewy Candy a good relief for sore throat and nausea.

Now, other than a great design, we also welcome brand suggestions for the candy.
If you can come up with a logo for the Ginger Candy, that would be swell!

We are open to unique and out of the box design. We chose a few color schemes for the design, but feel free to step out of the box if you feel it suits the brand.

We don't have the exact size for the plastic pouch, but it should be a generic small plastic pouch size (approximately 4 oz resealable plastic pouch)

Please have fun designing the project, we can't wait to see all the great designs!

Cheers!

Target Market(s)

USA and Asian market
Age 30-70
Male and Female

Industry/Entity Type

Manufacture

Font styles to use
Serif
Sans Serif
Decorative

Colors
fff3d1
fee18a
fece3e
fbc994
fce8d3

Requirements
Must have
• Torvel Logo
• A picture of ginger (illustrations or photographs are welcome)
Nice to have
• Coating suggestions like Matte surface or SPOT UV
• Give us ideas of what the name of the chewy candy should be. Product name ideas are welcome!

```html
<!DOCTYPE html>
<html lang="en">
<head>
<meta charset="utf-8">
<title>Torvel Ginger Chewy Candy – Pouch Front</title>
<link href="https://fonts.googleapis.com/css2?family=Lilita+One&family=Lobster&family=Montserrat:wght@400;600;800&display=swap" rel="stylesheet">
<style>
  :root {
    --page: #ffffff;
    --sun-light: #fff3a0;
    --sun-mid: #fee12a;
    --sun-deep: #fbc21a;
    --orange-base: #f7b21c;
    --brand-red: #a5161a;
    --brand-red-bright: #d4231f;
    --brand-red-dark: #6e0d10;
    --ink-dark: #2e2a26;
    --zip-dark: #1e1c1a;
    --zip-metal: #b89a55;
    --char-skin: #f2c198;
    --char-outline: #4a4642;
    --type-yellow: #ffe45c;
    --brand-navy: #2b3a8c;
  }
  * { margin: 0; padding: 0; box-sizing: border-box; }
  html, body { width: 1200px; height: 1000px; overflow: hidden; background: var(--page); }
  .canvas { position: relative; width: 1200px; height: 1000px; }

  .pouch-front {
    position: absolute; left: 321px; top: 60px; width: 558px; height: 880px; overflow: hidden;
    background: radial-gradient(ellipse 75% 55% at 50% 42%, var(--sun-light) 0%, var(--sun-mid) 55%, var(--sun-deep) 100%);
  }
  .sunburst-bg {
    position: absolute; inset: 0;
    background: linear-gradient(180deg, rgba(255,255,255,0) 60%, var(--orange-base) 100%);
  }
  .zip-track {
    position: absolute; left: 0; top: 92px; width: 558px; height: 12px;
    background: var(--zip-dark); border-top: 2px solid #f0e7c0; border-bottom: 2px solid #f0e7c0;
  }
  .zip-pull {
    position: absolute; left: 44px; top: 89px; width: 26px; height: 18px;
    background: var(--zip-metal); border-radius: 4px;
  }
  .zip-label {
    position: absolute; right: 46px; top: 74px;
    font: 400 10px/1 "Montserrat", sans-serif; color: #6b6456; letter-spacing: 0.02em;
  }
  .claim-natural {
    position: absolute; left: 140px; top: 170px;
    font: 800 19px/1 "Montserrat", sans-serif; color: var(--brand-red); letter-spacing: 0.32em;
  }
  .brand-name {
    position: absolute; left: 362px; top: 222px;
    font: 800 34px/1 "Montserrat", sans-serif; color: var(--brand-navy);
  }
  .title-backing {
    position: absolute; left: 62px; top: 238px; width: 420px; height: 318px;
    border-radius: 48% 52% 46% 54% / 40% 44% 56% 60%;
    background: radial-gradient(ellipse at 50% 45%, var(--brand-red-bright) 0%, var(--brand-red) 75%);
    box-shadow: 0 0 0 8px var(--sun-light);
  }
  .product-title {
    position: absolute; left: 62px; top: 238px; width: 420px; height: 318px;
    font-family: "Lobster", cursive; font-weight: 400; color: var(--type-yellow);
    text-shadow: 3px 4px 0 var(--brand-red-dark);
  }
  .product-title span { position: absolute; display: block; line-height: 1; white-space: nowrap; }
  .title-ginger { left: 18px; top: 10px; font-size: 120px; transform: rotate(-5deg); }
  .title-chewy { left: 58px; top: 150px; font-size: 62px; transform: rotate(-8deg); }
  .title-candy { left: 170px; top: 172px; font-size: 116px; transform: rotate(-5deg); }

  .mascot {
    position: absolute; left: 134px; top: 508px; width: 156px; height: 262px;
    border-radius: 45% 45% 50% 50%;
    background: var(--char-skin); border: 5px solid var(--char-outline);
  }
  .benefit-callout {
    position: absolute; left: 292px; top: 636px; transform: rotate(-6deg); transform-origin: left top;
    font: 400 27px/0.98 "Lilita One", sans-serif; color: var(--type-yellow); text-transform: uppercase;
    text-shadow: -2px -2px 0 var(--brand-red), 2px -2px 0 var(--brand-red), -2px 2px 0 var(--brand-red), 2px 2px 0 var(--brand-red), 4px 4px 0 var(--brand-red-dark);
  }
  .benefit-callout .line-indent { display: block; padding-left: 24px; }
  .benefit-callout .line-large { display: block; font-size: 32px; }
  .gluten-badge { position: absolute; left: 66px; top: 744px; width: 48px; text-align: center; }
  .gluten-badge svg { display: block; margin: 0 auto; }
  .gluten-badge span {
    display: block; margin-top: 6px; white-space: nowrap; margin-left: -10px; width: 68px;
    font: 600 9px/1 "Montserrat", sans-serif; color: var(--ink-dark);
  }
  .net-weight {
    position: absolute; right: 14px; top: 790px;
    font: 600 15px/1 "Montserrat", sans-serif; color: var(--ink-dark);
  }
</style>
</head>
<body>
<main class="canvas">
  <section class="pouch-front">
    <div class="sunburst-bg" role="img" aria-label="Yellow sunburst rays with soft orange clouds along the bottom"></div>
    <div class="zip-track"></div>
    <div class="zip-pull"></div>
    <p class="zip-label">ZIP LOCK SYSTEM</p>
    <p class="claim-natural">100% NATURAL</p>
    <p class="brand-name">Torvel</p>
    <div class="title-backing"></div>
    <h1 class="product-title">
      <span class="title-ginger">Ginger</span>
      <span class="title-chewy">chewy</span>
      <span class="title-candy">candy</span>
    </h1>
    <div class="mascot" role="img" aria-label="Cartoon ginger root character giving a thumbs up"></div>
    <p class="benefit-callout">
      <span class="line-indent">Good relief</span>
      <span class="line-indent">for sore</span>
      <span class="line-large" style="padding-left:12px">Throat &amp;</span>
      <span class="line-large">Nausea</span>
    </p>
    <div class="gluten-badge">
      <svg width="46" height="46" viewBox="0 0 46 46" aria-hidden="true">
        <circle cx="23" cy="23" r="20" fill="#fde37a" stroke="#2e2a26" stroke-width="2.5"/>
        <line x1="23" y1="12" x2="23" y2="36" stroke="#2e2a26" stroke-width="2"/>
        <line x1="9" y1="9" x2="37" y2="37" stroke="#2e2a26" stroke-width="2.5"/>
      </svg>
      <span>GLUTEN FREE</span>
    </div>
    <p class="net-weight">NET WT 4,4 OZ/124 G</p>
  </section>
</main>
</body>
</html>
```